Brambleton Business Card

I have a current card that I like it just needs a couple little changes to make it perfect. I would like the font size bigger so it could be easily read by older customers.

Business

```html
<!DOCTYPE html>
<html lang="en">
<head>
<meta charset="utf-8">
<title>Brambleton Motorsports and Marine – Business Card</title>
<link rel="stylesheet" href="https://fonts.googleapis.com/css2?family=Arimo:wght@400;700&family=Questrial&display=swap">
<style>
  :root {
    --ink: #000000;
    --paper: #ffffff;
    --band: #d9d9d9;
  }
  html, body {
    margin: 0;
    padding: 0;
    width: 1200px;
    height: 771px;
    overflow: hidden;
    background: var(--paper);
  }
  .card {
    position: relative;
    width: 1200px;
    height: 771px;
    background: var(--paper);
    color: var(--ink);
    font-family: "Arimo", Arial, sans-serif;
  }
  .company {
    position: absolute;
    left: 14px;
    top: 30px;
    width: 690px;
    text-align: center;
  }
  .company-name {
    margin: 0;
    font-size: 38px;
    font-weight: 700;
    line-height: 1.1;
  }
  .company-web {
    margin: 10px 0 0;
    font-size: 30px;
    font-weight: 700;
  }
  .contact-lines {
    position: absolute;
    left: 728px;
    top: 26px;
  }
  .contact-line {
    display: flex;
    align-items: center;
    height: 62px;
    margin-bottom: 4px;
    font-size: 38px;
    font-weight: 700;
    letter-spacing: 1px;
    white-space: nowrap;
  }
  .contact-line svg {
    width: 54px;
    height: 54px;
    margin-right: 12px;
    flex: none;
  }
  .brand-mark {
    position: absolute;
    left: 40px;
    top: 185px;
    width: 580px;
    height: 430px;
    display: flex;
    align-items: center;
    justify-content: center;
    gap: 22px;
  }
  .brand-dot {
    width: 54px;
    height: 54px;
    border-radius: 50%;
    background: var(--ink);
    flex: none;
  }
  .brand-word {
    font-size: 80px;
    font-weight: 700;
    line-height: 1;
  }
  .seasons-badge {
    position: absolute;
    left: 797px;
    top: 196px;
    width: 223px;
    height: 224px;
    box-sizing: border-box;
    border: 3px solid var(--ink);
    border-radius: 8px;
    padding: 9px;
  }
  .seasons-art {
    width: 100%;
    height: 100%;
    background: linear-gradient(135deg, #1a1a1a, #3a3a3a);
  }
  .tagline {
    position: absolute;
    left: 700px;
    top: 436px;
    width: 420px;
    text-align: center;
    font-family: "Questrial", "Century Gothic", sans-serif;
    font-size: 38px;
    margin: 0;
  }
  .person-band {
    position: absolute;
    left: 556px;
    top: 548px;
    width: 638px;
    height: 136px;
    background: var(--band);
    text-align: center;
    font-family: "Questrial", "Century Gothic", sans-serif;
  }
  .person-name {
    margin: 6px 0 0;
    font-size: 60px;
    line-height: 1.15;
  }
  .person-email {
    margin: 0;
    font-size: 37px;
    white-space: nowrap;
  }
  .address {
    position: absolute;
    left: 556px;
    top: 700px;
    width: 638px;
    text-align: center;
    margin: 0;
    font-size: 30px;
    font-weight: 700;
    white-space: nowrap;
  }
  .address sup {
    font-size: 18px;
  }
</style>
</head>
<body>
<main class="card">
  <header class="company">
    <h1 class="company-name">Brambleton Motorsports and Marine</h1>
    <p class="company-web">www.brambletonmotorsports.com</p>
  </header>

  <div class="contact-lines">
    <div class="contact-line phone">
      <svg viewBox="0 0 50 50" aria-hidden="true">
        <path d="M14 4 L22 4 L24 16 L18 20 Q21 30 27 36 L32 31 L44 34 L44 42 Q42 47 36 46 Q18 42 8 22 Q4 10 9 6 Z" fill="var(--ink)"/>
      </svg>
      <span>555 - 014 - 2876</span>
    </div>
    <div class="contact-line fax">
      <svg viewBox="0 0 50 50" aria-hidden="true">
        <rect x="16" y="3" width="22" height="18" fill="var(--paper)" stroke="var(--ink)" stroke-width="2"/>
        <rect x="3" y="19" width="44" height="28" rx="3" fill="var(--ink)"/>
        <rect x="5" y="22" width="9" height="22" rx="2" fill="var(--paper)"/>
        <rect x="19" y="24" width="24" height="6" fill="var(--paper)"/>
        <g fill="var(--paper)">
          <rect x="19" y="34" width="5" height="3"/><rect x="28" y="34" width="5" height="3"/><rect x="37" y="34" width="5" height="3"/>
          <rect x="19" y="40" width="5" height="3"/><rect x="28" y="40" width="5" height="3"/><rect x="37" y="40" width="5" height="3"/>
        </g>
      </svg>
      <span>555 - 014 - 3391</span>
    </div>
  </div>

  <div class="brand-mark">
    <span class="brand-dot"></span>
    <span class="brand-word">Brambleton</span>
  </div>

  <div class="seasons-badge">
    <div class="seasons-art" role="img" aria-label="Four-panel seasons illustration: a spring leaf, a summer sun, an autumn maple leaf and a winter snowflake"></div>
  </div>
  <p class="tagline">Fun For All Seasons</p>

  <section class="person-band">
    <p class="person-name">Dan Halvorsen</p>
    <p class="person-email">dan@brambletonmotorsports.com</p>
  </section>

  <p class="address">2841 162<sup>nd</sup> Street West Fernhollow, MN 5981</p>
</main>
</body>
</html>
```